Logo & Visitenkarte für ein Ingenieurbüro
Zielgruppe
Ich bin freiberuflich als Ingenieurbüro unterwegs. Projekte, Planungen erneuerbare Energien, Verbrauchsanalysen, Beratungen. Keine spezielle Zielgruppe. Grundthemen: Technik, Menschen, Netzwerk Verbinden
Aufgabenstellung
Das Design soll klar, vertrauensvoll, wertig, sysmpatisch sein.
Grundthemen: Technik, Menschen, Netzwerk, Verbinden
Rückseite: QR-Code von mir kommt dann nach Beratung

```html
<!DOCTYPE html>
<html lang="de">
<head>
<meta charset="utf-8">
<title>Jonas Wendler – Visitenkarte</title>
<link rel="stylesheet" href="https://fonts.googleapis.com/css2?family=Montserrat:wght@400;500;700&display=swap">
<style>
  :root {
    --green: #5aa84a;
    --green-light: #74b35f;
    --green-brand: #3db54a;
    --orange: #e0962e;
    --card-white: #f4f5f7;
    --stage: #ececec;
    --page: #ffffff;
    --text-light: #ffffff;
  }
  * { box-sizing: border-box; margin: 0; padding: 0; }
  html, body { width: 1200px; height: 1199px; overflow: hidden; }
  body {
    font-family: "Montserrat", Arial, sans-serif;
    background: var(--page);
    position: relative;
  }
  .stage {
    position: absolute; left: 0; top: 0;
    width: 1200px; height: 900px;
    background: var(--stage);
  }
  .card {
    position: absolute;
    width: 500px; height: 323px;
    border-radius: 4px;
    overflow: hidden;
    box-shadow: 0 6px 20px rgba(0,0,0,0.12);
  }
  /* Back side */
  .card--back { left: 70px; top: 290px; background: linear-gradient(135deg, var(--green) 0%, var(--green-light) 100%); }
  .contact-list {
    position: absolute; left: 48px; top: 150px;
    list-style: none; color: var(--text-light);
    font-size: 15px; line-height: 25px; font-weight: 500;
  }
  .contact-list li { position: relative; padding-left: 20px; }
  .contact-list li::before {
    content: ""; position: absolute; left: 0; top: 10px;
    width: 5px; height: 5px; border-radius: 50%; background: var(--text-light);
  }
  .card--back .emblem-area {
    position: absolute; right: -40px; top: -20px;
    width: 230px; height: 330px; border-radius: 50%;
    background: radial-gradient(circle at 55% 45%, rgba(255,255,255,0.85) 0%, rgba(255,255,255,0.35) 55%, rgba(255,255,255,0) 72%);
  }
  /* Front side */
  .card--front { left: 630px; top: 290px; background: var(--card-white); }
  .name-band {
    position: absolute; left: 0; top: 104px;
    width: 318px; height: 64px;
    background: var(--green);
    display: flex; align-items: center; gap: 14px;
    padding-left: 26px;
  }
  .name-band .mark-square { width: 30px; height: 30px; background: var(--text-light); }
  .name-band .name {
    color: var(--text-light); font-weight: 700;
    font-size: 19px; line-height: 20px; letter-spacing: 0.5px;
  }
  .title {
    position: absolute; left: 26px; top: 180px;
    color: var(--green); font-weight: 500; font-size: 18px;
  }
  .card--front .emblem-area {
    position: absolute; right: -30px; top: 30px;
    width: 200px; height: 300px; border-radius: 50%;
    background: radial-gradient(circle at 55% 50%, var(--orange) 0%, rgba(224,150,46,0.55) 35%, rgba(116,179,95,0.45) 60%, rgba(116,179,95,0) 74%);
  }
  /* Logo lockup */
  .lockup {
    position: absolute; left: 0; top: 990px; width: 1200px;
    display: flex; justify-content: center; align-items: center; gap: 36px;
  }
  .lockup .mark-square { width: 86px; height: 86px; background: var(--green-brand); }
  .lockup .name {
    color: var(--green-brand); font-weight: 700;
    font-size: 52px; line-height: 54px; letter-spacing: 1px;
  }
</style>
</head>
<body>
  <section class="stage">
    <article class="card card--back">
      <ul class="contact-list">
        <li>02351-48 210</li>
        <li>0171 204 3317</li>
        <li>info@j-wendler.de</li>
        <li>Brahmsweg 14,<br>58507 Feldhagen</li>
      </ul>
      <div class="emblem-area" role="img" aria-label="Emblem: Blatt und Blitz im Kreis, hell auf Grün"></div>
    </article>

    <article class="card card--front">
      <div class="name-band">
        <span class="mark-square"></span>
        <span class="name">JONAS<br>WENDLER</span>
      </div>
      <p class="title">Dipl. Ing. E-Technik</p>
      <div class="emblem-area" role="img" aria-label="Emblem: grünes Blatt mit Kreisbogen und orangem Blitz"></div>
    </article>
  </section>

  <div class="lockup">
    <span class="mark-square"></span>
    <span class="name">JONAS<br>WENDLER</span>
  </div>
</body>
</html>
```